Meridane Works, Inc. - Update our Website

Meridane Works needs a website to help our customers to navigate through our services efficiently. Our existing website is at www.meridwork.example

We would like to explain our services with content and pictures (photographs) that distinguishes our products and services from our competition.

The website design must implement a strategy to focus on our Contract Labeling services.

With this new design we would like to attract new customers and ensure that our existing customers are fully informed with our latest offerings.

```html
<!DOCTYPE html>
<html lang="en">
<head>
<meta charset="utf-8">
<title>Meridane Works, Inc.</title>
<link href="https://fonts.googleapis.com/css2?family=Open+Sans:wght@400;600;700&family=Tinos&display=swap" rel="stylesheet">
<style>
:root{
  --orange:#f07a1c;
  --orange-dark:#e0620e;
  --blue:#0a5fc4;
  --blue-deep:#063f94;
  --blue-light:#3a8ce0;
  --green:#8cc63f;
  --green-dark:#6ea82a;
  --ink:#222;
  --text:#555;
  --muted:#777;
  --link:#1a6fb5;
  --accent:#f05a28;
  --footer-green:#7aa62a;
  --band:#eeeeee;
  --line:#dddddd;
}
*{margin:0;padding:0;box-sizing:border-box}
html,body{width:1200px;height:2283px;overflow:hidden;background:#fff}
body{font-family:"Open Sans",Arial,sans-serif;color:var(--text);position:relative}
h1,h2,h3,h4{font-weight:400}
.abs{position:absolute}

/* top bar */
.topbar{left:0;top:0;width:1200px;height:30px;background:linear-gradient(var(--orange),var(--orange-dark))}
.topbar .contact{position:absolute;top:7px;font-size:12px;line-height:16px;color:#fff;display:flex;align-items:center;gap:8px;white-space:nowrap}
.topbar .social{position:absolute;top:7px;left:968px;display:flex;gap:6px}
.topbar .social span{width:16px;height:16px;border-radius:50%;background:rgba(255,255,255,.85)}

/* header */
.brand{display:flex;align-items:center;gap:10px;font-weight:700;color:#333;letter-spacing:.5px}
.brand .dot{border-radius:50%;background:var(--green)}
.header-brand{left:150px;top:62px;font-size:17px}
.header-brand .dot{width:26px;height:26px}
.nav{left:620px;top:72px;display:flex;gap:17px;font-size:13px;color:#333}

/* hero */
.hero{left:0;top:122px;width:1200px;height:378px;background:linear-gradient(180deg,var(--blue-light) 0%,var(--blue) 45%,var(--blue-deep) 100%);border-bottom:6px solid var(--green)}
.hero-title{left:210px;top:210px;font-family:"Tinos",serif;font-size:36px;color:#0a2550}
.hero-sub{left:210px;top:260px;font-size:20px;color:#fff}
.hero-text{left:210px;top:295px;width:340px;font-size:13px;line-height:18px;color:#fff}
.btn{display:flex;align-items:center;justify-content:center;gap:6px;background:var(--green);color:#fff;font-size:13px}
.hero-btn{left:210px;top:352px;width:150px;height:42px}
.hero-visual{left:665px;top:150px;width:360px;height:320px;border-radius:10px;background:radial-gradient(circle at 55% 45%,#e8eef5 0%,#9fb4cc 40%,rgba(10,95,196,0) 72%)}

/* intro */
.intro-title{left:0;top:520px;width:1200px;text-align:center;font-size:24px;color:#333}
.intro-text{left:270px;top:558px;width:660px;text-align:center;font-size:12px;line-height:16px;color:var(--muted)}

/* products band */
.band{left:0;top:625px;width:1200px;height:66px;background:var(--band)}
.band-title{left:258px;top:642px;font-size:27px;color:#333}

/* cards */
.card{width:260px}
.card h3{font-size:15px;font-weight:600;color:var(--link);margin-bottom:6px}
.card .photo{height:170px;border-radius:2px}
.card p{margin-top:14px;font-size:11.5px;line-height:16px;color:var(--text);height:64px}
.card .btn{margin-top:38px;width:152px;height:42px}

/* about */
.rule{height:1px;background:var(--line)}
.about-brand{left:100px;top:1745px;font-size:28px}
.about-brand .dot{width:40px;height:40px}
.about-divider{left:555px;top:1632px;width:1px;height:270px;background:var(--line)}
.about-title{left:628px;top:1645px;font-size:30px;color:#333}
.about-text{left:622px;top:1710px;width:440px;font-size:12px;line-height:18px;color:var(--text)}
.about-links{left:624px;top:1808px;display:grid;grid-template-columns:156px 200px;row-gap:10px;font-size:12px;color:var(--accent)}

/* footer */
.fcol h4{font-size:13px;color:var(--footer-green);margin-bottom:20px}
.fcol li{list-style:none;font-size:11px;line-height:19px;color:#444}
.fsocial{display:flex;gap:6px}
.fsocial span{width:18px;height:18px;border-radius:50%;background:#888}
.footer-divider{left:710px;top:2015px;width:1px;height:190px;background:var(--line)}
.footer-brand{left:845px;top:2035px;font-size:15px}
.footer-brand .dot{width:22px;height:22px}
.address{left:850px;top:2093px;font-size:10.5px;line-height:15px;color:#444;font-style:normal}
.copyright{left:122px;top:2252px;font-size:10.5px;color:#555}
</style>
</head>
<body>

<div class="abs topbar">
  <div class="contact" style="left:640px">
    <svg width="16" height="12" viewBox="0 0 16 12"><rect x="1" y="1" width="14" height="10" fill="none" stroke="#fff" stroke-width="1.5"/><path d="M1 1l7 6 7-6" fill="none" stroke="#fff" stroke-width="1.5"/></svg>
    info@meridwork.example
  </div>
  <div class="contact" style="left:828px">
    <svg width="12" height="14" viewBox="0 0 12 14"><path d="M3 1l2 3-1.5 1.5c.8 1.8 2 3 3.5 3.8L8.5 8l3 2-1.5 3C5 12 1 7.5 1 2z" fill="#fff"/></svg>
    1-555-018-2290
  </div>
  <div class="social"><span></span><span></span><span></span><span></span><span></span></div>
</div>

<div class="abs brand header-brand"><span class="dot"></span>MERIDANE WORKS</div>
<nav class="abs nav"><span>Home</span><span>About Us</span><span>Services</span><span>Products</span><span>User Support</span><span>Contact Us</span></nav>

<section class="abs hero"></section>
<div class="abs hero-visual" role="img" aria-label="Desktop monitor showing the company name, with a stethoscope and medicine capsules"></div>
<h1 class="abs hero-title">Meridane Works, Inc.</h1>
<p class="abs hero-sub">Leading Clinical Label Generation System</p>
<p class="abs hero-text">Meridane Works, Inc. specializes in providing products and services to the pharmaceutical industry.</p>
<div class="abs btn hero-btn">Learn More <span>+</span></div>

<h2 class="abs intro-title">We are focused on the needs of those individuals involved with Clinical Trial Materials.</h2>
<p class="abs intro-text">Lorem ipsum dolor sit amet, consectetur adipiscing elit. In rhoncus risus et elementum dapibus. Nulla facilisi. Mauris elementum eros justo, id pretium massa mattis quis. Morbi at semper dolor, ac pretium augue.</p>

<div class="abs band"></div>
<svg class="abs" style="left:170px;top:625px" width="64" height="66" viewBox="0 0 64 66"><path d="M0 0h34l30 33-30 33H0l30-33z" fill="#fff"/></svg>
<h2 class="abs band-title">Our Products &amp; Services</h2>

<article class="abs card" style="left:170px;top:727px">
  <h3>MeriServ™</h3>
  <div class="photo" role="img" aria-label="Doctor in a white coat using a tablet" style="background:linear-gradient(135deg,#eef1f4,#b7c2cc)"></div>
  <p>MeriServ™ is a contract clinical label generation service that provides you with ready to apply clinical labels specifically designed and produced for your clinical...</p>
  <div class="btn">Learn More <span>+</span></div>
</article>
<article class="abs card" style="left:465px;top:727px">
  <h3>MeriBook™</h3>
  <div class="photo" role="img" aria-label="Stack of shiny compact discs" style="background:linear-gradient(135deg,#7a2fa8,#d46ad8 50%,#4a7ad8)"></div>
  <p>MeriBook™ labels are multi-page clinical labels used to address the needs of multi-language studies. This enables user to prepare and ship clinical materials to multiple...</p>
  <div class="btn">Learn More <span>+</span></div>
</article>
<article class="abs card" style="left:755px;top:727px">
  <h3>Clinical Randomizations</h3>
  <div class="photo" role="img" aria-label="Glowing blue data grid" style="background:linear-gradient(135deg,#0a1f6a,#2c5fd8 55%,#8a3cc8)"></div>
  <p>Our systems can create randomization data for all types of CTM requirements. Patient randomization, material randomization and random...</p>
  <div class="btn">Learn More <span>+</span></div>
</article>

<article class="abs card" style="left:170px;top:1162px">
  <h3>MeriPro/LBL™</h3>
  <div class="photo" role="img" aria-label="Clear glass slide on a blue surface" style="background:linear-gradient(135deg,#0c3a8a,#5b8fd8 60%,#c9d8ee)"></div>
  <p>MeriServ™ is a contract clinical label generation service that provides you with ready to apply clinical labels specifically designed and produced for your clinical...</p>
  <div class="btn">Learn More <span>+</span></div>
</article>
<article class="abs card" style="left:465px;top:1162px">
  <h3>Software Validation Services</h3>
  <div class="photo" role="img" aria-label="Stethoscope lying on a computer keyboard" style="background:linear-gradient(135deg,#2a2e33,#6b7178 55%,#2a2e33)"></div>
  <p>MeriBook™ labels are multi-page clinical labels used to address the needs of multi-language studies. This enables user to prepare and ship clinical materials to multiple...</p>
  <div class="btn">Learn More <span>+</span></div>
</article>
<article class="abs card" style="left:755px;top:1162px">
  <h3>MeriStock™</h3>
  <div class="photo" role="img" aria-label="Close-up of a red die" style="background:radial-gradient(circle at 45% 55%,#c0392b,#7a1410 60%,#d9c7a8)"></div>
  <p>Our systems can create randomization data for all types of CTM requirements. Patient randomization, material randomization and random...</p>
  <div class="btn">Learn More <span>+</span></div>
</article>

<div class="abs rule" style="left:0;top:1578px;width:1200px"></div>
<div class="abs brand about-brand"><span class="dot"></span>MERIDANE WORKS</div>
<div class="abs about-divider"></div>
<h2 class="abs about-title">About Us</h2>
<p class="abs about-text">Meridane Works, Inc. specializes in providing products and services to the pharmaceutical industry. We are focused on the needs of those individuals involved with Clinical Trial Materials. Our products and services are summarized below:</p>
<div class="abs about-links">
  <span>MeriServ™</span><span>Clinical Randomizations</span>
  <span>MeriBook™</span><span>Software Validation Services</span>
  <span>MeriPro/LBL™</span><span>MeriStock™</span>
</div>

<div class="abs rule" style="left:0;top:1985px;width:1200px"></div>
<div class="abs fcol" style="left:122px;top:2023px">
  <h4>Navigation</h4>
  <ul><li>Home</li><li>About Us</li><li>Services</li><li>Products</li><li>User Support</li><li>Contact Us</li></ul>
</div>
<div class="abs fcol" style="left:288px;top:2023px">
  <h4>Products &amp; Services</h4>
  <ul><li>MeriServ</li><li>MeriBook</li><li>Randomizations</li><li>MeriPro/LBL Validation</li><li>MeriStock</li></ul>
</div>
<div class="abs fcol" style="left:500px;top:2023px">
  <h4>Follow us</h4>
  <div class="fsocial"><span></span><span></span><span></span><span></span><span></span></div>
</div>
<div class="abs footer-divider"></div>
<div class="abs brand footer-brand"><span class="dot"></span>MERIDANE WORKS</div>
<address class="abs address">
  512 ALDER LANE SUITE 40 BROOKFIELD<br>NY 10990-1122 USA<br><br>
  88 HARBOR ROW WESTMONT<br>NJ 08001 USA<br><br>
  PHONE: &nbsp;+1-555-014-7730<br>
  FAX: &nbsp;&nbsp;&nbsp;&nbsp;&nbsp;+1-555-014-7731
</address>
<p class="abs copyright">© 2014 Meridane Works, Inc. All rights reserved.</p>

</body>
</html>
```